Bright Harbor Notes Wordpress Blog

I need to design a WordPress blog page. The name of the Blog is "Bright Harbor Notes". I am hoping for a simple design that is easy for me to post future posts to. I like the color teal for this. The website is brightharbornotes.example where I am going to write a personal blog. I don't have a logo for this, but am hoping for a header that has some swirly, but classy looking text. Easy on the eyes. The website will only have a couple of pages - the home landing page, and an about me page.

Font styles to use
Script

Colors
00a990
86cfc6
cfeae6

Requirements
Must have
• A header for the landing page of the blog. Clean layout of where the blog posts will lie.

```html
<!DOCTYPE html>
<html lang="en">
<head>
<meta charset="utf-8">
<title>Bright Harbor Notes</title>
<link rel="stylesheet" href="https://fonts.googleapis.com/css2?family=Lobster&family=Oswald:wght@300;400&family=Raleway:wght@500;600;700&family=Noto+Serif:ital,wght@0,400;0,700;1,400&display=swap">
<style>
:root{
  --teal:#00a990;
  --teal-soft:#86cfc6;
  --teal-pale:#cfeae6;
  --ink:#4a4a4a;
  --body-text:#7a7a7a;
  --meta:#8a90a3;
  --panel:#ececec;
  --button:#e3e3e3;
  --frame:#dadada;
  --dark:#565656;
  --white:#ffffff;
  --rule:#e2e2e2;
}
*{box-sizing:border-box;margin:0;padding:0}
html,body{width:1200px;height:3041px;overflow:hidden;background:var(--white)}
body{position:relative;font-family:"Noto Serif",Georgia,serif;color:var(--ink)}
.abs{position:absolute}

/* top bar */
.topbar{left:0;top:0;width:1200px;height:82px;background:var(--teal)}
.site-name{left:73px;top:16px;font-family:"Lobster",cursive;font-size:31px;color:var(--white);letter-spacing:.3px}
.nav{right:0;top:0;height:82px;display:flex}
.nav a{display:block;height:82px;line-height:82px;padding:0 21px;font-family:"Raleway",sans-serif;font-weight:600;font-size:13px;color:var(--white);text-decoration:none;text-transform:uppercase;letter-spacing:.5px}
.nav a.current{background:var(--teal-pale);color:var(--teal);padding:0 18px}

/* hero */
.hero{left:0;top:82px;width:1200px;height:368px;background:linear-gradient(180deg,#6d7b82 0%,#9a8e78 30%,#d9a64e 58%,#f0c764 72%,#b9a044 82%,#4e6b2c 92%,#2f4a1c 100%)}
.hero-frame{left:20px;top:30px;width:1156px;height:298px;border:2px solid rgba(255,255,255,.8)}
.hero-title{left:0;width:1200px;top:110px;text-align:center;font-family:"Oswald",sans-serif;font-weight:300;font-size:48px;color:var(--white);letter-spacing:1px;text-transform:uppercase}
.hero-sub{left:0;width:1200px;top:164px;text-align:center;font-family:"Raleway",sans-serif;font-weight:500;font-size:20px;color:var(--white)}
.hero-rule{left:570px;top:194px;width:60px;height:2px;background:var(--white)}
.hero-date{left:0;width:1200px;top:202px;text-align:center;font-style:italic;font-size:12px;color:var(--white)}

/* common post parts */
.post-title{font-family:"Oswald",sans-serif;font-weight:300;font-size:20px;text-transform:uppercase;letter-spacing:.6px;color:#555;text-align:center;white-space:nowrap}
.divider{display:block;margin:0 auto}
.post-date{font-style:italic;font-size:11px;color:#9a9a9a;text-align:center}
.photo{border:5px solid var(--frame)}
.excerpt{font-size:13.5px;line-height:23px;color:var(--body-text)}
.meta{display:flex;align-items:center;gap:7px;font-family:"Raleway",sans-serif;font-weight:500;font-size:11.5px;color:var(--meta)}
.meta .gap{width:16px}
.avatar-sm{width:24px;height:24px;border-radius:50%;background:linear-gradient(135deg,#6b5548,#2f2622)}
.btn{display:flex;align-items:center;justify-content:center;gap:14px;background:var(--button);font-family:"Raleway",sans-serif;font-weight:700;font-size:11.5px;letter-spacing:1px;color:#333;text-transform:uppercase}
.btn svg{width:14px;height:10px}

/* featured */
.featured{left:36px;top:499px;width:775px;height:792px;background:var(--panel)}

/* grid cards */
.card{width:344px}
.card .post-title{position:absolute;left:0;width:344px;top:0}
.card .divider{position:absolute;left:107px;top:39px}
.card .post-date{position:absolute;left:0;width:344px;top:70px}
.card .photo{position:absolute;left:0;top:115px;width:344px;height:200px}
.card .excerpt{position:absolute;left:0;top:339px;width:344px}
.card .meta{position:absolute;left:2px;top:506px}
.card .btn{position:absolute;left:2px;top:558px;width:338px;height:33px}

.older{left:353px;top:2674px;width:140px;height:34px;background:var(--teal);color:var(--white);font-family:"Raleway",sans-serif;font-weight:700;font-size:11px;letter-spacing:.8px;display:flex;align-items:center;justify-content:center}

/* sidebar */
.side-rule{left:863px;top:517px;width:1px;height:2341px;background:var(--rule)}
.widget-head{left:904px;width:254px;height:35px;background:var(--teal);color:var(--white);font-family:"Oswald",sans-serif;font-weight:400;font-size:17px;text-transform:uppercase;letter-spacing:.5px;display:flex;align-items:center;justify-content:center}
.widget-head::after{content:"";position:absolute;left:120px;bottom:-7px;border-left:7px solid transparent;border-right:7px solid transparent;border-top:7px solid var(--teal)}
.portrait{left:945px;top:612px;width:174px;height:174px;border-radius:50%;background:radial-gradient(circle at 50% 45%,#cfcfcf,#7d7d7d 70%,#4a4a4a);border:3px solid #eee}
.role{left:904px;width:254px;top:806px;text-align:center;font-weight:700;font-size:11px;letter-spacing:.6px;color:#444}
.bio{left:904px;width:254px;top:838px;text-align:center;font-size:13.5px;line-height:23px;color:var(--body-text)}

.search{left:904px;top:1127px;width:254px;height:37px;display:flex}
.search .field{flex:1;background:#eaeaea;border:1px solid #dcdcdc;display:flex;align-items:center;justify-content:center;font-style:italic;font-size:12px;color:#999}
.search .go{width:42px;background:var(--dark);display:flex;align-items:center;justify-content:center}

.subscribe{left:904px;top:1310px;width:254px;height:215px;background:var(--dark);border:3px solid #6d6d6d}
.subscribe p{position:absolute;left:10px;width:228px;top:22px;text-align:center;color:var(--white);font-size:13.5px;line-height:22.5px}
.subscribe .email{position:absolute;left:18px;top:111px;width:212px;height:22px;background:var(--white);font-size:11.5px;color:#aaa;padding-left:6px;line-height:22px}
.subscribe .follow{position:absolute;left:12px;top:154px;width:224px;height:36px;background:var(--white);color:#555;font-family:"Raleway",sans-serif;font-weight:700;font-size:11px;letter-spacing:.8px;display:flex;align-items:center;justify-content:center}

.recent{left:904px;width:254px;display:flex;gap:16px}
.recent .icon{width:33px;height:33px;flex:none;background:#ececec;display:flex;align-items:center;justify-content:center;margin-top:4px}
.recent h4{font-weight:700;font-size:12.5px;line-height:19.5px;color:#444}
.recent .when{font-style:italic;font-size:11px;color:#a0a0a0;margin-top:6px}

.tags{left:904px;top:2290px;width:254px;display:flex;flex-wrap:wrap;gap:9px 8px}
.tags span{border:1px solid var(--teal-soft);padding:3px 8px;font-size:12.5px;color:#555;line-height:18px}

.cats{left:910px;top:2658px;list-style:none;font-size:13.5px;color:#555}
.cats li{height:36.5px}
.cats b{font-weight:400;color:var(--teal)}

/* footer */
.footer{left:0;top:2889px;width:1200px;height:152px;background:var(--teal)}
.social{left:0;width:1200px;top:34px;display:flex;justify-content:center;gap:22px;font-family:"Raleway",sans-serif;font-weight:700;font-size:12px;color:var(--white);text-transform:uppercase}
.social span{display:flex;align-items:center;gap:6px}
.social i{width:12px;height:12px;background:var(--white);display:block}
.foot-rule{left:44px;top:97px;width:1112px;height:1px;background:rgba(255,255,255,.5)}
.copyright{left:0;width:1200px;top:115px;text-align:center;font-family:"Raleway",sans-serif;font-weight:600;font-size:11px;color:var(--white);letter-spacing:.3px}
</style>
</head>
<body>

<svg width="0" height="0" style="position:absolute">
  <defs>
    <symbol id="diamond-rule" viewBox="0 0 130 18">
      <line x1="0" y1="9" x2="55" y2="9" stroke="#86cfc6" stroke-width="1.5"/>
      <line x1="75" y1="9" x2="130" y2="9" stroke="#86cfc6" stroke-width="1.5"/>
      <rect x="59" y="3" width="12" height="12" transform="rotate(45 65 9)" fill="none" stroke="#86cfc6" stroke-width="1.5"/>
    </symbol>
    <symbol id="cal" viewBox="0 0 12 12"><rect x="1" y="2" width="10" height="9" fill="none" stroke="#8a90a3" stroke-width="1.3"/><line x1="1" y1="5" x2="11" y2="5" stroke="#8a90a3" stroke-width="1.3"/></symbol>
    <symbol id="bubble" viewBox="0 0 12 12"><circle cx="6" cy="6" r="5.5" fill="#8a90a3"/><circle cx="3.6" cy="6" r="0.9" fill="#fff"/><circle cx="6" cy="6" r="0.9" fill="#fff"/><circle cx="8.4" cy="6" r="0.9" fill="#fff"/></symbol>
    <symbol id="arrow" viewBox="0 0 14 10"><line x1="0" y1="5" x2="12" y2="5" stroke="#00a990" stroke-width="1.4"/><polyline points="8,1 12,5 8,9" fill="none" stroke="#00a990" stroke-width="1.4"/></symbol>
    <symbol id="lines" viewBox="0 0 16 14"><rect x="0" y="0" width="16" height="2" fill="#00a990"/><rect x="0" y="4" width="16" height="2" fill="#00a990"/><rect x="0" y="8" width="16" height="2" fill="#00a990"/><rect x="0" y="12" width="10" height="2" fill="#00a990"/></symbol>
  </defs>
</svg>

<header class="abs topbar">
  <div class="abs site-name">Bright Harbor Notes</div>
  <nav class="abs nav">
    <a class="current">Home</a><a>About</a><a>Blogs</a><a>Contact</a>
  </nav>
</header>

<section class="abs hero" role="img" aria-label="Photo of a person leaping over a grassy hilltop against a golden sunset sky">
  <div class="abs hero-frame"></div>
  <h1 class="abs hero-title">Personality Growth</h1>
  <div class="abs hero-sub">A Major Aspect in Our Life</div>
  <div class="abs hero-rule"></div>
  <div class="abs hero-date">March 12th, 2017..... Reading Time Less than 2 mins.</div>
</section>

<!-- featured post -->
<article class="abs featured">
  <h2 class="abs post-title" style="left:0;width:775px;top:40px">Lorem Ipsum is simply dummy text of the printing and typesetting industry</h2>
  <svg class="abs" style="left:322px;top:80px" width="130" height="18"><use href="#diamond-rule"/></svg>
  <div class="abs post-date" style="left:0;width:775px;top:118px">March 12th, 2017..... Reading Time Less than 2 mins.</div>
  <div class="abs" role="img" aria-label="Photo of a woman in a hat walking down wooden garden steps" style="left:27px;top:156px;width:717px;height:466px;border:4px solid var(--teal-soft);background:linear-gradient(160deg,#7d9a4a 0%,#b7c77a 30%,#8a7f6c 55%,#c9bda8 75%,#5d5a4f 100%)"></div>
  <p class="abs excerpt" style="left:29px;top:642px;width:717px">Lorem Ipsum is simply dummy text of the printing and typesetting industry. Lorem Ipsum has been the industry's standard dummy text ever since the 1500s, when an unknown printer took a galley of type and scrambled it to make a type specimen book.</p>
  <div class="abs btn" style="left:29px;top:741px;width:195px;height:35px">Read More <svg><use href="#arrow"/></svg></div>
  <div class="abs meta" style="left:431px;top:746px">
    <span class="avatar-sm" role="img" aria-label="Author photo"></span><span>milo</span><span class="gap"></span>
    <svg width="12" height="12"><use href="#cal"/></svg><span>May 22, 2016</span><span class="gap"></span>
    <svg width="12" height="12"><use href="#bubble"/></svg><span>0 Comments</span>
  </div>
</article>

<!-- grid posts -->
<article class="abs card" style="left:65px;top:1356px">
  <h2 class="post-title">Feugiat vitae ultricies eget</h2>
  <svg class="divider" width="130" height="18"><use href="#diamond-rule"/></svg>
  <div class="post-date">March 12th, 2017..... Reading Time Less than 2 mins.</div>
  <div class="photo" role="img" aria-label="Photo of a person writing at a desk in a purple sweater" style="background:linear-gradient(120deg,#4a2a22 0%,#7b4a3a 35%,#e9e3dc 60%,#6f3f7a 100%)"></div>
  <p class="excerpt">Lorem Ipsum is simply dummy text of the printing and typesetting industry. Lorem Ipsum has been the industry's standard dummy text ever since the 1500s, when an unknown printer took a galley of type and scrambled it to make a type specimen book.</p>
  <div class="meta"><span class="avatar-sm" role="img" aria-label="Author photo"></span><span>milo</span><span class="gap"></span><svg width="12" height="12"><use href="#cal"/></svg><span>May 22, 2016</span><span class="gap"></span><svg width="12" height="12"><use href="#bubble"/></svg><span>0 Comments</span></div>
  <div class="btn">Read More <svg><use href="#arrow"/></svg></div>
</article>

<article class="abs card" style="left:450px;top:1356px">
  <h2 class="post-title">Online Video Post</h2>
  <svg class="divider" width="130" height="18"><use href="#diamond-rule"/></svg>
  <div class="post-date">March 12th, 2017..... Reading Time Less than 2 mins.</div>
  <div class="photo" role="img" aria-label="Video still of a figure silhouetted against bright sunlight on a hillside" style="background:radial-gradient(circle at 55% 30%,#f4e2b8 0%,#b89a6e 25%,#4a3f33 60%,#1f1a16 100%)"></div>
  <p class="excerpt">Lorem Ipsum is simply dummy text of the printing and typesetting industry. Lorem Ipsum has been the industry's standard dummy text ever since the 1500s, when an unknown printer took a galley of type and scrambled it to make a type specimen book.</p>
  <div class="meta"><span class="avatar-sm" role="img" aria-label="Author photo"></span><span>milo</span><span class="gap"></span><svg width="12" height="12"><use href="#cal"/></svg><span>May 22, 2016</span><span class="gap"></span><svg width="12" height="12"><use href="#bubble"/></svg><span>0 Comments</span></div>
  <div class="btn">Read More <svg><use href="#arrow"/></svg></div>
</article>

<article class="abs card" style="left:65px;top:2040px">
  <h2 class="post-title">Vidora HD Video Post</h2>
  <svg class="divider" width="130" height="18"><use href="#diamond-rule"/></svg>
  <div class="post-date">March 12th, 2017..... Reading Time Less than 2 mins.</div>
  <div class="photo" role="img" aria-label="Video player still of people gathered in a dim room" style="background:linear-gradient(100deg,#2a2420 0%,#6a5548 40%,#c9b3a3 55%,#3a302a 100%)"></div>
  <p class="excerpt">Lorem Ipsum is simply dummy text of the printing and typesetting industry. Lorem Ipsum has been the industry's standard dummy text ever since the 1500s, when an unknown printer took a galley of type and scrambled it to make a type specimen book.</p>
  <div class="meta"><span class="avatar-sm" role="img" aria-label="Author photo"></span><span>milo</span><span class="gap"></span><svg width="12" height="12"><use href="#cal"/></svg><span>May 22, 2016</span><span class="gap"></span><svg width="12" height="12"><use href="#bubble"/></svg><span>0 Comments</span></div>
  <div class="btn">Read More <svg><use href="#arrow"/></svg></div>
</article>

<article class="abs card" style="left:450px;top:2040px">
  <h2 class="post-title">Online Video Post</h2>
  <svg class="divider" width="130" height="18"><use href="#diamond-rule"/></svg>
  <div class="post-date">March 12th, 2017..... Reading Time Less than 2 mins.</div>
  <div class="photo" role="img" aria-label="Photo of a woman jumping on a sunny beach" style="background:linear-gradient(180deg,#6fa8d8 0%,#9cc6e6 55%,#3e8fb3 68%,#d8c7a4 80%,#c7b28a 100%)"></div>
  <p class="excerpt">Lorem Ipsum is simply dummy text of the printing and typesetting industry. Lorem Ipsum has been the industry's standard dummy text ever since the 1500s, when an unknown printer took a galley of type and scrambled it to make a type specimen book.</p>
  <div class="meta"><span class="avatar-sm" role="img" aria-label="Author photo"></span><span>milo</span><span class="gap"></span><svg width="12" height="12"><use href="#cal"/></svg><span>May 22, 2016</span><span class="gap"></span><svg width="12" height="12"><use href="#bubble"/></svg><span>0 Comments</span></div>
  <div class="btn">Read More <svg><use href="#arrow"/></svg></div>
</article>

<div class="abs older">OLDER POSTS</div>

<!-- sidebar -->
<div class="abs side-rule"></div>

<h3 class="abs widget-head" style="top:525px">About Me</h3>
<div class="abs portrait" role="img" aria-label="Black and white portrait of the blogger in a sun hat"></div>
<div class="abs role">BLOGGER</div>
<p class="abs bio">Lorem Ipsum is simply dummy text of the printing and typesetting industry. Lorem Ipsum has been the industry's standard dummy text ever since the 1500s, when an unknown printer</p>

<h3 class="abs widget-head" style="top:1056px">Search</h3>
<div class="abs search">
  <div class="field">Enter Keyword</div>
  <div class="go"><svg width="16" height="16" viewBox="0 0 16 16"><circle cx="6.5" cy="6.5" r="4.5" fill="none" stroke="#fff" stroke-width="1.8"/><line x1="10" y1="10" x2="14.5" y2="14.5" stroke="#fff" stroke-width="2"/></svg></div>
</div>

<h3 class="abs widget-head" style="top:1249px">Subscribe</h3>
<div class="abs subscribe">
  <p>Subscribe and get all our content and tutorials for free and without spam.</p>
  <div class="email">Enter your email address</div>
  <div class="follow">FOLLOW ME!</div>
</div>

<h3 class="abs widget-head" style="top:1614px">Recent Posts</h3>
<div class="abs recent" style="top:1686px"><div class="icon"><svg width="16" height="14"><use href="#lines"/></svg></div><div><h4>Pellentesque habitant morbi tristique senectus et netus</h4><div class="when">February 18, 2017.</div></div></div>
<div class="abs recent" style="top:1787px"><div class="icon"><svg width="16" height="14"><use href="#lines"/></svg></div><div><h4>Vestibulum tortor quam, feugiat vitae, ultricies eget</h4><div class="when">February 18, 2017.</div></div></div>
<div class="abs recent" style="top:1870px"><div class="icon"><svg width="16" height="14"><use href="#lines"/></svg></div><div><h4>Donec eu libero sit amet quam egestas semper. Aenean ultricies mi vitae.</h4><div class="when">February 18, 2017.</div></div></div>
<div class="abs recent" style="top:1980px"><div class="icon"><svg width="16" height="14"><use href="#lines"/></svg></div><div><h4>Pellentesque habitant morbi tristique senectus et netus</h4><div class="when">February 18, 2017.</div></div></div>
<div class="abs recent" style="top:2081px"><div class="icon"><svg width="16" height="14"><use href="#lines"/></svg></div><div><h4>Vestibulum tortor quam, feugiat vitae, ultricies eget</h4><div class="when">February 18, 2017.</div></div></div>

<h3 class="abs widget-head" style="top:2220px">Tags</h3>
<div class="abs tags">
  <span>Art</span><span>Blogging</span><span>Colours</span><span>Dresser</span><span>Illustration</span><span>Inspiration</span><span>Minimal</span><span>Model</span><span>Stories</span><span>Tech</span><span>Themes</span><span>Tutorials</span><span>Typography</span><span>Video</span><span>Web design</span>
</div>

<h3 class="abs widget-head" style="top:2577px">Categories</h3>
<ul class="abs cats">
  <li>Fantasy <b>(4)</b></li>
  <li>Inspiration <b>(6)</b></li>
  <li>Things <b>(5)</b></li>
  <li>Travel <b>(4)</b></li>
</ul>

<footer class="abs footer">
  <div class="abs social">
    <span><i></i>Circlebook</span><span><i></i>Chirper</span><span><i></i>Tackwall</span><span><i></i>Snapframe</span><span><i></i>Shotdeck</span><span><i></i>Tunewave</span><span><i></i>Streamly</span>
  </div>
  <div class="abs foot-rule"></div>
  <div class="abs copyright">© COPYRIGHT 2017 ALL RIGHTS RESERVED</div>
</footer>

</body>
</html>
```